Kindle Grove Wording For Logo & Business card

I have the logo, I just need the "kindle Grove" wording to go with it, and a business card design. The only thing on the business card is the website info. We provide nature connection experiences, and bolster these efforts through writing and host a platform for community around it.

I also have an idea of what it could look like (sketch), though I'm really not sure how it would come out. I am open to the best design and happy to consider original artwork. You can see what the site is about at KindleGrove.com.

Contact Information for Business Card

The only thing on the business card is the website info and the design. I will put other messaging on the back.

Website lettering (KindleGrove.com) in Montserrat

Logo Text

Kindle Grove (letters optional)

Font styles to use
Other font styles liked:
• montserrat

```html
<!DOCTYPE html>
<html lang="en">
<head>
<meta charset="utf-8">
<title>Kindle Grove – Business Card</title>
<link href="https://fonts.googleapis.com/css2?family=Montserrat:wght@500;800&display=swap" rel="stylesheet">
<style>
  :root {
    --backdrop: #2a2a2c;
    --card: #120d24;
    --gold: #f7b418;
    --ember: #f0741c;
    --rule: #ffffff;
  }
  * { margin: 0; padding: 0; box-sizing: border-box; }
  html, body {
    width: 1200px;
    height: 900px;
    overflow: hidden;
    background: var(--backdrop);
  }
  .stage {
    width: 1200px;
    height: 900px;
    display: flex;
    align-items: center;
    justify-content: center;
  }
  .business-card {
    position: relative;
    width: 980px;
    height: 560px;
    background: var(--card);
    border-radius: 36px;
    display: flex;
    flex-direction: column;
    align-items: center;
    justify-content: center;
    font-family: "Montserrat", sans-serif;
  }
  .brand {
    display: flex;
    align-items: center;
    gap: 22px;
    margin-top: -40px;
  }
  .brand-rule {
    width: 130px;
    height: 2px;
    background: var(--rule);
  }
  .brand-dot {
    width: 46px;
    height: 46px;
    border-radius: 50%;
    background: var(--ember);
  }
  .brand-name {
    font-weight: 800;
    font-size: 64px;
    letter-spacing: 2px;
    text-transform: uppercase;
    color: var(--gold);
    line-height: 1;
  }
  .website {
    position: absolute;
    bottom: 88px;
    font-weight: 500;
    font-size: 26px;
    letter-spacing: 2px;
    color: var(--gold);
  }
</style>
</head>
<body>
  <main class="stage">
    <section class="business-card">
      <div class="brand">
        <span class="brand-rule"></span>
        <span class="brand-dot"></span>
        <span class="brand-name">Kindle Grove</span>
        <span class="brand-rule"></span>
      </div>
      <p class="website">www.KindleGrove.com</p>
    </section>
  </main>
</body>
</html>
```